Label: Tiko "ZAP" Ruvel

Everyone missed the mark: Lets try this one I just made for you. The dog is all I could find but looks too mean. You will need to replace with a large happy dog. the bottle I am using is Oval shaped with a flip lid, Wetted dog food in bowl must shine ... Need art work for 2" X 2 " plastic bottle labels and art to post on my web site This is a dry powder you mix with water and squeeze on dry dog food, Imagine the "WOW" is in a large, friendly, now very happy dogs open mouth. I am sharing with you my first version I had created using a dog chef that looks cheap, old fashioned and is missing the "WOW" factor. Think Thick, Glossy, Bright Bold Colors. I want a new progressive look adding a quick splash of taste to otherwise boring dog food.

Target Market(s)

stop and get the attention of dog owners shopping for kibble in pet stores and on line orders that they need to buy this for their dog to add Flavor to old boring dry dog food

Requirements
Must have
• Sorry, Tiko "ZAP" Ruvel is correct spelling for product trademark and "TikoRuvel"
is our company name. Bottle is Oval with flip lid, dog must be replaced with large happy dog., "WOW" in mouth should look better but still funny. You should chuckle.
Wetted dog food in bowl should shine and look glossy. made in USA needs clear flag I have art work. I like bright colors not pastels or bland ones.
Nice to have
• Clean professional bright humorous with product clearly represented
Should not have
• Boring, old, cheap looking, outdated, limiting by not appealing to all demographics, lacking color,

```html
<!DOCTYPE html>
<html lang="en">
<head>
<meta charset="utf-8">
<title>Tiko "ZAP" Ruvel – Instant Beef Au Jus</title>
<link rel="stylesheet" href="https://fonts.googleapis.com/css2?family=Bangers&family=Oswald:wght@600;700&display=swap">
<style>
  :root{
    --orange:#f39a1e;
    --orange-deep:#e2690d;
    --red:#e3281b;
    --red-deep:#b5140c;
    --yellow:#ffd23d;
    --white:#ffffff;
    --ink:#1a1a1a;
    --brown:#6b3a1c;
    --steel:#9aa0a6;
  }
  *{margin:0;padding:0;box-sizing:border-box}
  html,body{width:1200px;height:1200px;overflow:hidden;background:var(--white)}
  .ad{
    position:relative;width:1200px;height:1200px;overflow:hidden;
    background:radial-gradient(circle at 50% 52%, #fffbe8 0%, #ffd77a 22%, var(--orange) 55%, var(--orange-deep) 100%);
    font-family:"Oswald", sans-serif;color:var(--ink);
  }
  .brand-box{
    position:absolute;left:100px;top:36px;width:980px;height:170px;
    background:var(--white);border:10px solid var(--orange);border-radius:18px;
    display:flex;align-items:center;justify-content:center;gap:26px;
    box-shadow:0 6px 0 var(--orange-deep);
  }
  .brand-name{font-family:"Bangers", cursive;font-size:118px;letter-spacing:4px;color:var(--ink);line-height:1}
  .brand-dot{width:34px;height:34px;border-radius:50%;background:var(--red)}

  .dog-photo{
    position:absolute;left:230px;top:250px;width:650px;height:560px;border-radius:40% 40% 30% 30%;
    background:radial-gradient(ellipse at 50% 45%, #a5652e 0%, #7a4520 55%, #3b2414 100%);
  }
  .bottle-hand{
    position:absolute;left:840px;top:190px;width:360px;height:560px;border-radius:60px 0 0 60px;
    background:linear-gradient(160deg, #e8b58c 0%, #c86a1c 45%, #8e3a0c 100%);
  }
  .bowl{
    position:absolute;left:320px;top:770px;width:580px;height:300px;border-radius:50%;
    background:radial-gradient(ellipse at 50% 40%, #a0451a 0%, var(--brown) 45%, var(--steel) 70%, #5c6166 100%);
  }

  .burst{position:absolute;left:0;top:330px;width:480px;height:310px}
  .burst-text{
    position:absolute;left:40px;top:390px;width:400px;text-align:center;transform:rotate(-8deg);
    font-family:"Bangers", cursive;font-size:52px;line-height:1.05;color:var(--white);letter-spacing:1px;
    text-shadow:3px 3px 0 var(--red-deep);
  }

  .instant{position:absolute;left:130px;top:610px;font-size:34px;font-weight:700;color:var(--white);text-shadow:2px 2px 0 rgba(0,0,0,.35)}
  .beef{
    position:absolute;left:68px;top:648px;font-family:"Bangers", cursive;font-size:104px;line-height:1;letter-spacing:2px;
    color:var(--red);-webkit-text-stroke:3px var(--white);text-shadow:4px 4px 0 var(--red-deep);
  }
  .for-dry{position:absolute;left:130px;top:752px;font-size:34px;font-weight:700;color:var(--white);text-shadow:2px 2px 0 rgba(0,0,0,.35)}

  .wow{
    position:absolute;left:20px;top:790px;transform:rotate(-6deg);
    font-family:"Bangers", cursive;font-size:230px;line-height:1;letter-spacing:4px;
    color:var(--orange);-webkit-text-stroke:5px var(--white);text-shadow:8px 8px 0 var(--red);
  }

  .thanks{position:absolute;left:40px;top:1010px;width:290px;text-align:center;font-weight:700;color:var(--ink);line-height:1.1}
  .thanks .small{font-size:36px;display:block}
  .thanks .big{font-family:"Bangers", cursive;font-size:64px;color:var(--red);letter-spacing:1px;display:block}

  .seal{position:absolute;left:920px;top:700px;width:300px;height:320px}
  .seal-text{
    position:absolute;left:950px;top:770px;width:260px;text-align:center;transform:rotate(-10deg);
    font-family:"Bangers", cursive;color:var(--white);line-height:1;
  }
  .seal-text .line{font-size:42px;display:block}
  .seal-text .num{font-size:120px;display:block}

  .flavor{
    position:absolute;left:420px;top:1040px;transform:rotate(-7deg);
    font-family:"Bangers", cursive;font-size:72px;letter-spacing:2px;color:var(--orange);
    -webkit-text-stroke:3px var(--white);text-shadow:4px 4px 0 var(--red-deep);
  }

  .size{position:absolute;left:1070px;top:1060px;font-size:40px;font-weight:700;color:var(--ink)}
  .flag{position:absolute;left:1072px;top:1110px;width:64px;height:40px;background:linear-gradient(180deg,#c8232c 0 50%, #2b3f8f 50% 100%)}
  .made{position:absolute;left:1060px;top:1152px;width:96px;text-align:center;font-family:"Oswald", sans-serif;font-weight:600;font-size:18px;line-height:1.05;color:var(--ink)}
</style>
</head>
<body>
<main class="ad">
  <div class="dog-photo" role="img" aria-label="Large happy dog with open mouth and tongue out"></div>
  <div class="bottle-hand" role="img" aria-label="Hand squeezing an oval flip-lid bottle of beef au jus"></div>
  <div class="bowl" role="img" aria-label="Steel bowl of glossy wetted dry dog food"></div>

  <header class="brand-box">
    <span class="brand-name">Tiko "ZAP" Ruvel</span>
    <span class="brand-dot"></span>
  </header>

  <svg class="burst" viewBox="0 0 480 310" aria-hidden="true">
    <polygon fill="#e3281b" stroke="#ffffff" stroke-width="4"
      points="30,70 110,80 140,20 200,65 270,10 300,70 390,30 380,100 470,110 410,160 460,220 380,220 390,290 310,250 250,300 200,250 120,290 120,230 20,240 70,180 5,140 70,120"/>
  </svg>
  <p class="burst-text">JUST ADD WATER<br>SHAKE AND SQUEEZE!</p>

  <p class="instant">INSTANT FLAVORED</p>
  <p class="beef">BEEF AU JUS</p>
  <p class="for-dry">FOR DRY DOG FOOD</p>

  <p class="wow">WOW!</p>

  <p class="thanks">
    <span class="small">YOUR DOG WILL</span>
    <span class="big">THANK YOU</span>
    <span class="small">EVERYDAY!</span>
  </p>

  <svg class="seal" viewBox="0 0 300 320" aria-hidden="true">
    <polygon fill="#e3281b" stroke="#ffffff" stroke-width="6"
      points="160,5 185,35 222,20 232,58 272,60 266,100 298,122 276,155 296,190 262,208 266,248 226,252 212,290 176,276 150,310 124,280 86,296 76,256 36,250 42,212 6,192 28,158 6,124 40,104 34,64 74,60 86,22 122,36"/>
    <circle cx="152" cy="160" r="118" fill="none" stroke="#ffffff" stroke-width="4"/>
  </svg>
  <p class="seal-text">
    <span class="line">MAKES OVER</span>
    <span class="num">30</span>
    <span class="line">SERVINGS!</span>
  </p>

  <p class="flavor">SAVORY BEEF FLAVOR!</p>

  <p class="size">18 Oz.</p>
  <div class="flag" role="img" aria-label="United States flag"></div>
  <p class="made">Made In<br>the U.S.A</p>
</main>
</body>
</html>
```